tile distributor needs a new logo and packaging designe

"BREVALO TILE & STONE LTD'' in Canada needs great logo and a graphic design for a cardboard box package for the ceramic tiles. For inspiration you can use the logo from our sister's company, www.brevalo-example.de.
In regards to the cardboard package for the ceramic tiles it should include the BREVALO new logo on white cardboard background.
The box has to have the following info:
-Company name (with slogan "ARCHITECTURAL SOLUTIONS" or similar)
-Nominal size of the tiles (we need packages for 30cm x 60cm, 60cm x 60cm,and 30cm x 90cm) with table: nominal thickness, #pieces per box and MQ/SFT per box
-product description "RECTIFIED PORCELAIN TILE"
-made in china (not too visible, small letters)
-CE sign
-Attention text:"Before tile setting, please verify...." (see the attachment)
-Emission in indoor air sign
-and the hole on the front page (the color of the tile should be visible)
All text will be translated in 3 languages (German, English and Serbian)
I have attached some samples of the competitor"s packages and our current box for your reference.
I have increased the budget for CND$100 for my project and I hope that now it will be more atractiv for designers.
Looking forward to seeing your fresh ideas.
Reason: I have just increased the budget for this project therefore I am extending the deadline.
Hope this will help to get the great design for my company logo and packaging.

```html
<!DOCTYPE html>
<html lang="en">
<head>
<meta charset="utf-8">
<title>Brevalo – Rectified Porcelain Tile Box</title>
<link href="https://fonts.googleapis.com/css2?family=Open+Sans:wght@400;600;700;800&display=swap" rel="stylesheet">
<style>
  :root {
    --page-bg: #f2f2f2;
    --board: #ececec;
    --board-edge: #d9d9d9;
    --ink-slate: #5a6a70;
    --band: #2b3a3f;
    --band-line: #8d9aa0;
    --white: #ffffff;
    --brand-red: #b3242a;
    --tile-light: #e6dcc6;
    --tile-mid: #cfc3a6;
    --title-blue: #7f97a2;
    --badge: #e8b9a6;
  }
  * { box-sizing: border-box; margin: 0; padding: 0; }
  html, body { width: 1200px; height: 876px; overflow: hidden; }
  body {
    background: var(--page-bg);
    font-family: "Open Sans", Arial, sans-serif;
    position: relative;
  }

  .front-panel {
    position: absolute;
    left: 80px; top: 60px;
    width: 1040px; height: 520px;
    background: var(--board);
    border: 1px solid var(--board-edge);
  }
  .brand {
    position: absolute; left: 44px; top: 44px;
    display: flex; align-items: center; gap: 14px;
  }
  .brand-square { width: 64px; height: 64px; background: var(--brand-red); }
  .brand-name {
    font-size: 44px; font-weight: 400; letter-spacing: 4px;
    color: var(--ink-slate); line-height: 1;
  }
  .brand-slogan {
    font-size: 15px; font-weight: 400; letter-spacing: 1px;
    color: var(--ink-slate); margin-top: 6px;
  }
  .product-title {
    position: absolute; right: 44px; top: 52px;
    text-align: right; color: var(--ink-slate);
    font-weight: 800; font-size: 38px; line-height: 1.05;
  }
  .tile-window { position: absolute; left: 470px; top: 155px; }

  .info-band {
    position: absolute; left: 40px; right: 40px; top: 345px;
    height: 110px; background: var(--band);
    color: var(--white);
  }
  .spec-table {
    position: absolute; left: 12px; top: 14px;
    border-collapse: collapse; font-size: 15px; color: #cfd6d9;
  }
  .spec-table td {
    border: 1px solid var(--band-line);
    padding: 1px 8px; height: 27px;
  }
  .spec-table td.value { text-align: right; width: 62px; }
  .band-slogan {
    position: absolute; left: 280px; top: 26px;
    font-size: 24px; font-weight: 700; line-height: 1.1;
  }
  .nominal-size {
    position: absolute; right: 22px; top: 14px;
    font-size: 20px; font-weight: 400;
  }
  .nominal-size strong { font-size: 42px; font-weight: 800; margin-left: 8px; }
  .origin {
    position: absolute; right: 22px; bottom: 8px;
    font-size: 14px;
  }

  .side-panel {
    position: absolute;
    left: 80px; top: 610px;
    width: 1040px; height: 170px;
    background: var(--white);
    border: 1px solid var(--board-edge);
  }
  .emission-badge {
    position: absolute; left: 40px; top: 30px;
    width: 170px; height: 110px;
    border: 2px solid var(--badge);
    background: #fbeee8;
  }
  .side-title {
    position: absolute; left: 250px; top: 46px;
    color: var(--title-blue); font-weight: 800;
    font-size: 36px; line-height: 1;
  }
  .ce-mark {
    position: absolute; left: 640px; top: 60px;
    width: 60px; height: 46px; border-radius: 6px;
    background: #c9c9c9;
  }
  .side-brand { position: absolute; right: 40px; top: 54px; display: flex; align-items: center; gap: 12px; }
  .side-brand .brand-square { width: 52px; height: 52px; }
  .side-brand .brand-name { font-size: 36px; }
</style>
</head>
<body>
  <section class="front-panel">
    <div class="brand">
      <div class="brand-square"></div>
      <div>
        <div class="brand-name">BREVALO</div>
        <div class="brand-slogan">ARCHITECTURAL SOLUTIONS</div>
      </div>
    </div>

    <h1 class="product-title">RECTIFIED<br>PORCELAIN TILE</h1>

    <svg class="tile-window" width="530" height="160" viewBox="0 0 530 160" role="img" aria-label="Cut-out window showing the beige stone-look tile surface">
      <defs>
        <linearGradient id="tileTone" x1="0" y1="0" x2="1" y2="1">
          <stop offset="0" stop-color="var(--tile-light)"/>
          <stop offset="1" stop-color="var(--tile-mid)"/>
        </linearGradient>
      </defs>
      <polygon points="0,8 325,8 220,155 110,155" fill="url(#tileTone)"/>
      <polygon points="355,8 390,8 470,155 258,155" fill="url(#tileTone)"/>
      <polygon points="420,8 530,8 530,112 478,112" fill="url(#tileTone)"/>
    </svg>

    <div class="info-band">
      <table class="spec-table">
        <tr><td>Nominal thickness</td><td class="value">11</td></tr>
        <tr><td>Pieces</td><td class="value">8</td></tr>
        <tr><td>MQ</td><td class="value">0,810</td></tr>
      </table>
      <div class="band-slogan">ARCHITECTURAL<br>SOLUTIONS</div>
      <div class="nominal-size">Nominal size:<strong>30x60</strong></div>
      <div class="origin">made in china</div>
    </div>
  </section>

  <section class="side-panel">
    <div class="emission-badge"></div>
    <h2 class="side-title">RECTIFIED<br>PORCELAIN TILE</h2>
    <div class="ce-mark"></div>
    <div class="side-brand">
      <div class="brand-square"></div>
      <div class="brand-name">BREVALO</div>
    </div>
  </section>
</body>
</html>
```